Bold Website Redesign for a Disruptive Training Brand

Corvane Labs is a bold, no-fluff sales & leadership training company powered by AI-driven practice and behavioral science. We’ve already built our website structure and copy in Lovable.ai — now we need a designer to fully transform the visual design across all pages (Home, Approach, Programs, About, Contact).
We’re looking for a modern, memorable, high-performance aesthetic that blends human energy, science, and tech without feeling corporate or safe. Clean, bold typography, fluid layout, strong emotional hero moments, subtle motion, and imagery that mixes real people with abstract scientific/tech visuals.Because our clients are primarily North American, please ensure any human photography or AI-generated imagery reflects a North American business context and demographics (modern, diverse, and realistic).

Your job is visual redesign only — no coding required.
The final design must be practical to rebuild inside Lovable.ai.

A full, detailed creative brief (plus logo files) is included in the uploaded files.
If you can bring a mix of edge, intelligence, and strong visual storytelling, we’d love to see your work.

Website is already built in Lovable.ai at - https://corvane-website-tempdesign.plinkora-sites.app — structure is set, visuals need redesign.

Sick

```html
<!DOCTYPE html>
<html lang="en">
<head>
<meta charset="utf-8">
<title>Corvane Labs — Training That Practices Back</title>
<link href="https://fonts.googleapis.com/css2?family=Jost:wght@400;500;600;700&display=swap" rel="stylesheet">
<style>
:root{
  --navy:#14203a;
  --navy-deep:#101a30;
  --card-blue:#28406e;
  --white:#ffffff;
  --muted:#d5dcea;
  --blue:#3c63b0;
  --cyan:#3bb4dc;
  --grad:linear-gradient(90deg,#3c5fae 0%,#3bb3db 100%);
}
*{margin:0;padding:0;box-sizing:border-box}
html,body{width:1200px;height:3082px;overflow:hidden}
body{
  position:relative;font-family:'Jost',sans-serif;color:var(--white);
  background:
    radial-gradient(ellipse 520px 700px at 1200px 1050px,rgba(40,110,150,.45),transparent 70%),
    radial-gradient(ellipse 600px 500px at 600px 480px,rgba(30,60,110,.35),transparent 70%),
    var(--navy);
}
.abs{position:absolute}
.brand{font-weight:600;letter-spacing:3px;text-align:center;color:var(--white);line-height:1.15}
.brand-dot{display:block;width:26px;height:26px;border-radius:50%;background:var(--grad);margin:0 auto 8px}
.nav{top:46px;left:562px;display:flex;gap:35px;font-size:12px;font-weight:600;letter-spacing:.3px}
.btn{display:flex;align-items:center;justify-content:center;font-size:11.5px;font-weight:600;letter-spacing:.4px;border-radius:3px}
.btn-grad{background:var(--grad);color:var(--white)}
.btn-white{background:var(--white);color:#3a78c4}
.center{left:0;width:1200px;text-align:center}
h1,h2,h3{font-weight:700;text-transform:uppercase;letter-spacing:.3px}
.hero-title{top:172px;font-size:41px}
.hero-sub{top:224px;font-size:12px;font-weight:600}
.hero-text{top:250px;font-size:12px;line-height:19px;font-weight:400}
.wave{top:370px;left:0;width:1200px;height:230px;background:linear-gradient(90deg,transparent,rgba(60,110,200,.25) 20%,rgba(70,150,220,.35) 50%,rgba(60,110,200,.25) 80%,transparent);filter:blur(2px);clip-path:ellipse(50% 40% at 50% 50%)}
.play{left:539px;top:418px;width:124px;height:124px;border-radius:50%;border:2px solid var(--white);background:var(--navy-deep)}
.sec-title{font-size:31px;line-height:34px}
.sec-text{font-size:12px;line-height:19px}
.chart-card{left:163px;top:935px;width:874px;height:364px;background:var(--white);border-radius:20px}
.pill-card{border-radius:155px;background:linear-gradient(180deg,var(--card-blue) 0%,rgba(30,50,90,.4) 70%,transparent 100%);text-align:center}
.pill-card.mid{background:linear-gradient(0deg,#2d4d7d 0%,rgba(35,60,100,.4) 75%,transparent 100%)}
.pill-card h3{font-size:22px;margin-bottom:8px}
.pill-card p{font-size:15px;line-height:18px;color:var(--muted);padding:0 42px}
.icon{display:block;margin:0 auto}
.photo{left:609px;top:1951px;width:516px;height:388px;border-radius:22px;background:linear-gradient(135deg,#2a3f6e 0%,#1a2748 45%,#3a4a6a 70%,#1a2440 100%)}
.cta{left:75px;top:2466px;width:1050px;height:228px;border-radius:24px;background:linear-gradient(90deg,#3d5fae 0%,#3a8cc8 55%,#3bb4dc 100%)}
.footer h4{font-size:17px;font-weight:600;text-transform:uppercase;margin-bottom:12px}
.footer li{list-style:none;font-size:13px;line-height:23px}
.divider{left:102px;top:3026px;width:993px;height:1px;background:rgba(255,255,255,.25)}
</style>
</head>
<body>

<header>
  <div class="abs brand" style="left:70px;top:22px;width:135px;font-size:13px">
    <span class="brand-dot"></span>CORVANE<br><span style="font-size:10px;letter-spacing:4px">LABS</span>
  </div>
  <nav class="abs nav"><span>HOME</span><span>APPROACH</span><span>PROGRAMS</span><span>ABOUT</span><span>CONTACT</span></nav>
  <a class="abs btn btn-grad" style="left:997px;top:36px;width:111px;height:39px">LET'S TALK</a>
</header>

<section class="hero">
  <h1 class="abs center hero-title">Training that practices back.</h1>
  <p class="abs center hero-sub">AI-DRIVEN SUSTAINMENT THAT BUILDS MASTERY — SO YOU DON'T HAVE TO.</p>
  <p class="abs center hero-text">You'll see measurable growth as your people turn insight into habit — automatically,<br>sustainably, and without extra work for their leaders.</p>
  <a class="abs btn btn-grad" style="left:473px;top:303px;width:142px;height:39px">SEE HOW WE DO IT</a>
  <a class="abs btn btn-white" style="left:622px;top:303px;width:104px;height:39px">LET'S TALK</a>
  <div class="abs wave" role="img" aria-label="Flowing blue sound-wave lines across the hero"></div>
  <div class="abs play">
    <svg width="120" height="120" viewBox="0 0 120 120"><circle cx="60" cy="60" r="38" fill="none" stroke="#fff" stroke-width="1.5"/><path d="M51 44 L77 60 L51 76 Z" fill="#fff"/></svg>
  </div>
</section>

<section class="problem">
  <h2 class="abs center sec-title" style="top:715px">The real problem isn't your people<br>it's the forgetting curve.</h2>
  <p class="abs center sec-text" style="top:790px">Within a week, most training disappears. Leaders are left guessing who's using what they learned — and no one has time to fix it.<br>We built Corvane Labs to make progress automatic, measurable, and real.</p>
  <a class="abs btn btn-grad" style="left:410px;top:842px;width:380px;height:39px">WATCH HOW SUSTAINED PRACTICE CHANGES THE CURVE</a>
  <div class="abs chart-card">
    <svg width="874" height="364" viewBox="0 0 874 364" font-family="Jost, sans-serif">
      <rect x="20" y="10" width="834" height="344" rx="4" fill="#fff" stroke="#e2e4e8"/>
      <text x="33" y="34" font-size="8.5" fill="#555" font-weight="600" letter-spacing=".6">FUNNEL • JANUARY 1, 2024 - FEBRUARY 15, 2025</text>
      <rect x="730" y="28" width="10" height="8" fill="none" stroke="#555"/>
      <text x="745" y="36" font-size="10" fill="#444">Show details</text>
      <text x="824" y="34" font-size="12" fill="#555">•••</text>
      <rect x="33" y="61" width="52" height="13" rx="2" fill="#f3f8d9"/>
      <text x="40" y="71" font-size="8.5" fill="#7a8a20">ux-bench</text>
      <text x="33" y="90" font-size="9.5" fill="#333">Last modified a month ago by</text>
      <circle cx="180" cy="86" r="8" fill="#d9c8f0"/><text x="176.5" y="90" font-size="9" fill="#5b3a9a">O</text>
      <text x="193" y="90" font-size="9.5" fill="#333">you</text>
      <line x1="20" y1="107" x2="854" y2="107" stroke="#e2e4e8"/>
      <g font-size="8.5" fill="#333" text-anchor="end">
        <text x="54" y="129">60%</text><text x="54" y="161">50%</text><text x="54" y="193">40%</text><text x="54" y="226">30%</text><text x="54" y="258">20%</text><text x="54" y="290">10%</text><text x="54" y="322">0%</text>
      </g>
      <g stroke="#e6e8ec"><line x1="62" y1="126" x2="815" y2="126"/><line x1="62" y1="158" x2="815" y2="158"/><line x1="62" y1="190" x2="815" y2="190"/><line x1="62" y1="223" x2="815" y2="223"/><line x1="62" y1="255" x2="815" y2="255"/><line x1="62" y1="287" x2="815" y2="287"/></g>
      <line x1="62" y1="126" x2="62" y2="319" stroke="#999"/><line x1="62" y1="319" x2="815" y2="319" stroke="#999"/>
      <rect x="62" y="165" width="753" height="25" fill="#f5c6cb"/>
      <polyline fill="none" stroke="#3a45d6" stroke-width="1.3" points="62,163 120,164.6 178,151.7 236,148.5 294,155 352,166.2 409,169.4 467,171 525,161.4 583,177.5 641,175.8 699,179 757,182.3 815,185.5"/>
      <g font-size="8.5" fill="#333" text-anchor="middle">
        <text x="62" y="337">1-Jan-2024</text><text x="120" y="337">1-Feb-2024</text><text x="178" y="337">1-Mar-2024</text><text x="236" y="337">1-Apr-2024</text><text x="294" y="337">1-May-2024</text><text x="352" y="337">1-Jun-2024</text><text x="409" y="337">1-Jul-2024</text><text x="467" y="337">1-Aug-2024</text><text x="525" y="337">1-Sep-2024</text><text x="583" y="337">1-Oct-2024</text><text x="641" y="337">1-Nov-2024</text><text x="699" y="337">1-Dec-2024</text><text x="757" y="337">1-Jan-2025</text><text x="815" y="337">1-Feb-2025</text>
      </g>
    </svg>
  </div>
</section>

<section class="pillars">
  <h2 class="abs center sec-title" style="top:1410px">Practice made permanent.</h2>
  <p class="abs center sec-text" style="top:1447px">You'll replace "hope they remember" with a system that makes sure they do.</p>

  <div class="abs pill-card" style="left:135px;top:1508px;width:311px;height:292px;padding-top:60px">
    <svg class="icon" width="70" height="72" viewBox="0 0 70 72" fill="none" stroke="#fff" stroke-width="2"><circle cx="35" cy="18" r="10"/><path d="M31 28v6h8v-6"/><path d="M4 38h28l3 4 3-4h28v30H38l-3 3-3-3H4z"/><path d="M35 42v26M10 48h16M10 55h16M44 48h16M44 55h16"/></svg>
    <h3 style="margin-top:26px">Learn</h3>
    <p>Fast, focused workshops, built on science, that install the mindset and skills that matter most.</p>
  </div>

  <div class="abs pill-card mid" style="left:445px;top:1510px;width:310px;height:356px;padding-top:118px">
    <h3>Certify</h3>
    <p>Programmatic AI-driven practice and feedback - mastery without management overhead.</p>
    <svg class="icon" style="margin-top:22px" width="72" height="72" viewBox="0 0 72 72" fill="none" stroke="#fff" stroke-width="2"><rect x="16" y="4" width="44" height="54" rx="2"/><path d="M10 12v54h30"/><path d="M24 16h28M24 24h28M24 32h18"/><circle cx="50" cy="48" r="8"/><path d="M45 55l-3 12 8-4 8 4-3-12"/></svg>
  </div>

  <div class="abs pill-card" style="left:755px;top:1508px;width:311px;height:292px;padding-top:62px">
    <svg class="icon" width="72" height="70" viewBox="0 0 72 70" fill="none" stroke="#fff" stroke-width="2"><path d="M8 66h56"/><rect x="14" y="28" width="22" height="38"/><path d="M19 36h4M27 36h4M19 44h4M27 44h4M19 52h4M27 52h4"/><path d="M44 66V44c0-8 6-14 14-14"/><path d="M10 24C16 10 32 4 46 8l6 4"/><path d="M48 4l6 8-9 3"/></svg>
    <h3 style="margin-top:24px">Sustain</h3>
    <p>Light-touch challenges and dashboards that keep skills sharp long after training ends.</p>
  </div>
</section>

<section class="team">
  <h2 class="abs" style="left:129px;top:2020px;font-size:30px;line-height:34px">Built by people<br>who've led the change<br>themselves.</h2>
  <p class="abs sec-text" style="left:129px;top:2139px;width:430px">Behind Corvane Labs are leaders who've lived the challenge of making learning last. They've scaled companies, built cultures, and led transformation — and now they've designed the system they always wished existed.</p>
  <div class="abs brand" style="left:135px;top:2244px;font-size:18px;text-align:left;letter-spacing:3px">CORVANE LABS</div>
  <div class="abs photo" role="img" aria-label="Photo of a diverse business team gathered around a table in a dark modern office"></div>
</section>

<section class="abs cta">
  <div class="abs brand" style="left:110px;top:92px;width:260px;font-size:32px;letter-spacing:6px">CORVANE</div>
  <h2 class="abs" style="left:470px;top:52px;font-size:30px;line-height:34px">Ready to see what lasting<br>capability looks like?</h2>
  <a class="abs btn btn-white" style="left:472px;top:140px;width:186px;height:39px">START A CONVERSATION</a>
</section>

<footer class="footer">
  <div class="abs brand" style="left:160px;top:2794px;width:160px;font-size:14px">
    <span class="brand-dot"></span>CORVANE<br><span style="font-size:10px;letter-spacing:4px">LABS</span>
  </div>
  <p class="abs" style="left:125px;top:2876px;width:244px;font-size:11.5px;line-height:19px;text-align:center">Making learning that sticks through AI-driven sustainment and behavioral science.</p>
  <div class="abs" style="left:421px;top:2793px"><h4>Quick Links</h4><ul><li>Home</li><li>Approach</li><li>Programs</li><li>About</li><li>Contact</li></ul></div>
  <div class="abs" style="left:639px;top:2793px">
    <h4>Get In Touch</h4>
    <ul>
      <li><svg width="10" height="8"><rect width="10" height="8" fill="#3bb4dc"/></svg> contact@corvanelabs.com</li>
      <li style="margin-top:7px"><svg width="10" height="10" viewBox="0 0 10 10"><path d="M1 1l3 0 1 3-1.5 1 a6 6 0 0 0 2.5 2.5L7 6l3 1v2C5 10 0 5 1 1z" fill="#3bb4dc"/></svg> +1 (555) 014-2290</li>
      <li style="margin-top:7px;line-height:16px"><svg width="9" height="11" viewBox="0 0 9 11"><path d="M4.5 11C1 6 0 5 0 4.5a4.5 4.5 0 0 1 9 0C9 5 8 6 4.5 11z" fill="#3bb4dc"/></svg> 4870 Meridian Ave Suite 210<br><span style="padding-left:16px">Tempe, AZ 85281</span></li>
    </ul>
  </div>
  <div class="abs" style="left:951px;top:2793px">
    <h4>Follow Me</h4>
    <div style="display:flex;gap:8px;margin-left:2px"><span style="width:22px;height:22px;border-radius:50%;background:var(--blue)"></span><span style="width:22px;height:22px;border-radius:50%;background:var(--blue)"></span></div>
  </div>
  <div class="abs divider"></div>
  <p class="abs center" style="top:3046px;font-size:12px">© 2025 Corvane Labs. All rights reserved.</p>
  <div class="abs" style="left:1129px;top:3010px;width:34px;height:34px;border-radius:50%;background:var(--grad)">
    <svg width="34" height="34" viewBox="0 0 34 34"><path d="M14 19l3-3 3 3" fill="none" stroke="#fff" stroke-width="1.5"/></svg>
  </div>
</footer>

</body>
</html>
```